Refresh of The Marwick Partners business card

Update business card design using existing primary logo. Names, numbers, etc. are too hard to read on current design.

Target Market(s)

We are a CPA firm.

Industry/Entity Type

Accountant

Contact Information for Business Card

update current card

Colors
0355a3
3176b5
85acd3
0792cd

Requirements
Must have
• Easier to read phone numbers and names
• Use existing logo
Nice to have
• We love our color scheme and current TMP logo. But the names and phone numbers are too small and card just look old and stale.

```html
<!DOCTYPE html>
<html lang="en">
<head>
<meta charset="utf-8">
<title>The Marwick Partners — Business Card</title>
<link rel="stylesheet" href="https://fonts.googleapis.com/css2?family=Cinzel:wght@400;600&family=Questrial&display=swap">
<style>
  :root {
    --page: #e9e7e4;
    --card-white: #ffffff;
    --navy-deep: #0c2447;
    --navy: #14396e;
    --brand-blue: #0355a3;
    --brand-mid: #3176b5;
    --brand-light: #85acd3;
    --ink: #2a2f3a;
    --ink-soft: #4a5160;
    --white: #ffffff;
  }
  * { margin: 0; padding: 0; box-sizing: border-box; }
  html, body { width: 1200px; height: 997px; overflow: hidden; }
  body {
    background: var(--page);
    display: flex;
    flex-direction: column;
    align-items: center;
    justify-content: center;
    gap: 60px;
    font-family: "Questrial", "Century Gothic", sans-serif;
  }
  .card {
    width: 588px;
    height: 336px;
    position: relative;
    box-shadow: 0 6px 18px rgba(0,0,0,0.15);
    overflow: hidden;
  }

  /* Front */
  .card-front { background: var(--card-white); }
  .front-identity {
    position: absolute;
    left: 28px;
    top: 132px;
    width: 124px;
    display: flex;
    flex-direction: column;
    align-items: center;
    gap: 8px;
  }
  .logo-disc {
    width: 64px; height: 64px; border-radius: 50%;
    background: var(--brand-blue);
  }
  .logo-name {
    font-size: 11px;
    color: var(--navy);
    white-space: nowrap;
  }
  .person {
    position: absolute;
    left: 168px;
    top: 156px;
    font-family: "Cinzel", serif;
    color: var(--navy);
    text-align: center;
  }
  .person-name { font-size: 17px; font-weight: 600; letter-spacing: 0.5px; white-space: nowrap; }
  .person-title { font-size: 16px; margin-top: 2px; }
  .contact {
    position: absolute;
    left: 384px;
    top: 58px;
    color: var(--ink-soft);
    font-size: 12.5px;
    line-height: 1.45;
    white-space: nowrap;
  }
  .contact-firm { color: var(--navy); font-weight: 700; font-size: 13px; }
  .contact-list { list-style: none; margin-top: 8px; }
  .contact-list li { display: flex; align-items: center; gap: 7px; }
  .contact-list svg { width: 11px; height: 11px; flex: none; }

  /* Back */
  .card-back {
    background: radial-gradient(ellipse at 55% 40%, var(--brand-blue) 0%, var(--navy) 55%, var(--navy-deep) 100%);
  }
  .back-map {
    position: absolute; inset: 0;
    background: radial-gradient(ellipse at 50% 45%, rgba(133,172,211,0.12), rgba(133,172,211,0) 65%);
  }
  .back-lockup {
    position: absolute;
    left: 0; right: 0; top: 118px;
    display: flex; align-items: center; justify-content: center; gap: 16px;
  }
  .back-disc {
    width: 70px; height: 70px; border-radius: 50%;
    background: var(--white);
  }
  .back-name {
    font-size: 26px;
    color: var(--white);
    letter-spacing: 0.5px;
    line-height: 1;
    white-space: nowrap;
  }
  .back-tagline {
    font-size: 10px;
    letter-spacing: 2.5px;
    color: var(--white);
    text-transform: uppercase;
    margin-top: 8px;
    padding-top: 6px;
    border-top: 1px solid rgba(255,255,255,0.7);
    white-space: nowrap;
  }
  .back-web {
    position: absolute;
    left: 0; right: 0; top: 238px;
    text-align: center;
    color: var(--white);
    font-size: 17px;
    letter-spacing: 0.5px;
  }
  .back-rule {
    position: absolute;
    left: 214px; top: 266px;
    width: 160px; height: 1px;
    background: rgba(255,255,255,0.5);
  }
</style>
</head>
<body>

  <section class="card card-front" aria-label="Business card front">
    <div class="front-identity">
      <span class="logo-disc"></span>
      <span class="logo-name">The Marwick Partners</span>
    </div>
    <div class="person">
      <p class="person-name">Daniel R. Marwick</p>
      <p class="person-title">CPA</p>
    </div>
    <div class="contact">
      <p class="contact-firm">The Marwick Partners</p>
      <p>812 Lakeview Ave. Suite 310</p>
      <p>Winter Park, Florida 32789</p>
      <ul class="contact-list">
        <li><svg viewBox="0 0 12 12"><circle cx="6" cy="6" r="6" fill="#2a2f3a"/><path d="M4 3.2l1 1.3-.6.7c.4.9 1 1.5 1.9 1.9l.7-.6 1.3 1-.6 1.1C5.8 8.4 3.6 6.2 3 4z" fill="#fff"/></svg>407.555.0142</li>
        <li><svg viewBox="0 0 12 12"><circle cx="6" cy="6" r="6" fill="#2a2f3a"/><rect x="3" y="4" width="6" height="4" rx=".5" fill="#fff"/></svg>407.555.0178</li>
        <li><svg viewBox="0 0 12 12"><circle cx="6" cy="6" r="6" fill="#2a2f3a"/><rect x="4.3" y="2.8" width="3.4" height="6.4" rx=".6" fill="#fff"/></svg>407.555.0193</li>
        <li><svg viewBox="0 0 12 12"><circle cx="6" cy="6" r="6" fill="#2a2f3a"/><rect x="3" y="4" width="6" height="4" fill="none" stroke="#fff" stroke-width=".8"/><path d="M3 4l3 2.2L9 4" fill="none" stroke="#fff" stroke-width=".8"/></svg>dan@marwickpartners.com</li>
      </ul>
    </div>
  </section>

  <section class="card card-back" aria-label="Business card back">
    <div class="back-map" role="img" aria-label="Faint dotted world map in the background"></div>
    <div class="back-lockup">
      <span class="back-disc"></span>
      <div>
        <p class="back-name">The Marwick Partners</p>
        <p class="back-tagline">Certified Public Accountants</p>
      </div>
    </div>
    <p class="back-web">www.marwickpartners.com</p>
    <span class="back-rule"></span>
  </section>

</body>
</html>
```